I have a website called Nexa Holdings (nexaholdings.com) that I would like to have redesigned. Most of the content is already created, but I need a new design. You can also see my other website at corbelestates.com. I am open to a new logo or modifying the current logo if you have a good idea. Please feel free to use other images for the home page (and maybe some other locations) if you feel they provide a better look and feel to the website. I prefer a modern look.

Important: You do not have to use the images I've provided for the home page. Feel free to find your own stock photos. You don't have to pay for them unless I select your design.

1) Please use wix.com to make your changes so that I can edit it later.
2) I will need all the graphics files to be saved so I can dowload it for later.
3) I will be adding more content to the site later.
4) This site will likely be transferred over to corbelestates.com so if you make a logo please make one for Nexa Holdings and one for Corbel Estates.
5) You can use other images that you feel would help the look and feel of the website.

Real Estate

Coded - Design and coding required

5+ page

```html
<!DOCTYPE html>
<html lang="en">
<head>
<meta charset="utf-8">
<title>Nexa Holdings — Home</title>
<link href="https://fonts.googleapis.com/css2?family=Archivo+Black&family=Roboto:wght@300;400;500;700&display=swap" rel="stylesheet">
<style>
:root{
  --blue:#2a7db0;
  --blue-dark:#1b4e7c;
  --ink:#2b2b2b;
  --field:#f1f1f1;
  --white:#fff;
  --p-dark:#222;
  --p-green:#2fb37a;
  --p-navy:#2a3a6b;
  --p-crimson:#9c1d4a;
  --p-gold:#d3a12a;
}
*{margin:0;padding:0;box-sizing:border-box}
html,body{width:758px;height:1200px;overflow:hidden;background:var(--white)}
body{position:relative;font-family:'Roboto',sans-serif;color:var(--ink)}
.abs{position:absolute}

.topbar{left:0;top:0;width:758px;height:14px;background:var(--blue);color:var(--white);font-size:5.5px}
.topbar span{position:absolute;top:3.5px}
.social{position:absolute;top:4.5px;width:5px;height:5px;border-radius:50%;background:var(--white)}

.nav{top:14px;left:0;width:758px;height:39px;background:var(--white)}
.brand{display:flex;align-items:center;gap:4px;color:var(--blue);font-weight:500;white-space:nowrap}
.brand i{display:block;background:var(--blue)}
.menu a{position:absolute;top:15px;font-size:6.5px;color:var(--ink);text-decoration:none}
.menu .active{left:355px;top:13.5px;width:37px;height:12px;border-radius:6px;background:#e3eef7;text-align:center;line-height:12px;font-weight:500;color:var(--blue-dark)}

.hero{top:53px;left:0;width:758px;height:232px;overflow:hidden}
.hero h1{font-family:'Archivo Black',sans-serif;font-weight:400;color:var(--blue-dark);font-size:19.5px;line-height:24.6px;letter-spacing:.3px;left:57px;top:83px;white-space:nowrap}
.hero .tag{left:57px;top:160px;font-size:10.8px;color:#4a4a4a;font-weight:400}

.about{left:170px;top:265px;width:420px;height:106px;background:var(--white);border-radius:55px;box-shadow:0 2px 6px rgba(0,0,0,.13)}
.pill{background:var(--blue);color:var(--white);font-weight:700;border-radius:10px;text-align:center}
.about p{position:absolute;left:25px;top:37px;width:377px;font-size:6.5px;line-height:7.5px;text-align:justify;color:#444}

.projects-title{left:167px;top:410px;font-size:9px;font-weight:700;color:var(--blue)}
.projects-intro{left:167px;top:426px;width:182px;font-size:4.9px;line-height:6.3px;color:#333}
.view-all{left:552px;top:423px;width:36px;height:17px;border:1px solid #ddd;border-radius:9px;font-size:5.2px;text-align:center;line-height:15px}

.card{top:469.5px;width:135px}
.card .photo{height:93px;border-radius:6px;position:relative;overflow:hidden}
.card .badge{position:absolute;left:0;bottom:0;background:var(--white);border-radius:0 6px 0 0;padding:3px 7px;font-size:4.8px;display:flex;align-items:center;gap:3px;color:#444}
.card .badge b{width:5px;height:5px;border:1px solid #e33;border-radius:1px;display:block}
.card h3{font-size:5.3px;font-weight:500;margin-top:5px}
.card .type{font-size:4.2px;color:#1d45b5;margin-top:3.5px;font-weight:500}
.card p{font-size:5px;line-height:6.7px;color:#444;margin-top:3px;width:126px}

.partner{top:683px;width:70px;margin-left:-35px;text-align:center;font-size:9.5px;font-weight:700;line-height:12px}

.city{top:728px;left:0;width:758px;height:171px;background:linear-gradient(180deg,#2f7fca 0%,#2c74bd 45%,#2467a9 70%,#2a6fb5 100%)}
.map{left:167.5px;top:767.5px;width:241.5px;height:141.5px;border-radius:9px;background:linear-gradient(125deg,#eef1ea 0%,#e4eae2 40%,#dde5ee 52%,#b5cdec 60%,#9dbeea 68%,#c9d8ec 76%,#eceee8 86%,#e6eadf 100%)}

.info h4{position:absolute;left:167px;font-size:8px;font-weight:700;color:var(--blue)}
.info p{position:absolute;font-size:6.4px;line-height:7.5px;color:#333}

.contact-card{left:420px;top:767.5px;width:170px;height:260px;background:var(--white);border-radius:15px;box-shadow:0 2px 6px rgba(0,0,0,.08)}
.contact-card h2{position:absolute;left:0;width:170px;top:12px;text-align:center;font-size:8px;font-weight:500}
.field{position:absolute;left:8px;width:155px;height:18px;border-radius:9px;background:var(--field);font-size:6.2px;color:#888;padding:0 6px;line-height:18px}
.field.msg{line-height:normal;padding-top:5px}
.submit{position:absolute;left:8px;top:227px;width:155px;height:18px;border-radius:9px;background:var(--blue);color:var(--white);font-size:6.2px;font-weight:700;text-align:center;line-height:18px}

.footer{left:0;top:1088px;width:758px;height:112px;background:var(--blue);color:var(--white)}
.footer .lead{position:absolute;left:170px;top:62px;width:115px;font-size:5.5px;line-height:6.4px}
.footer h5{position:absolute;left:491px;top:27px;font-size:6.4px;font-weight:500}
.f-item{position:absolute;left:491px;display:flex;gap:5px;font-size:5.5px;line-height:6.4px}
.f-item svg{flex:none}
</style>
</head>
<body>
<div class="abs topbar">
  <span style="left:170px">Kết nối</span>
  <i class="social" style="left:191px"></i><i class="social" style="left:200px"></i><i class="social" style="left:209px"></i>
  <span style="left:455px">&#9742; 090 412 7730</span>
  <span style="left:515px">&#9993; careers@nexaholdings.com</span>
</div>

<header class="abs nav">
  <div class="abs brand" style="left:173px;top:13px;font-size:6.5px"><i style="width:11px;height:11px;border-radius:2px"></i>NEXA HOLDINGS</div>
  <nav class="menu">
    <a class="active">Home</a>
    <a style="left:413px">About</a>
    <a style="left:462px">Strategy</a>
    <a style="left:516px">Project</a>
    <a style="left:568px">Contact</a>
  </nav>
</header>

<section class="abs hero">
  <svg class="abs" style="left:0;top:0" width="758" height="232" viewBox="0 0 758 232">
    <defs>
      <linearGradient id="heroFade" x1="0" y1="0" x2="1" y2="1">
        <stop offset="0" stop-color="#dfe8ef"/>
        <stop offset=".45" stop-color="#eef3f7"/>
        <stop offset=".8" stop-color="#e4eaee"/>
        <stop offset="1" stop-color="#d6dadc"/>
      </linearGradient>
      <linearGradient id="heroPhoto" x1="0" y1="0" x2="0" y2="1">
        <stop offset="0" stop-color="#d7e6f2"/>
        <stop offset=".14" stop-color="#8e7a62"/>
        <stop offset=".4" stop-color="#5a5d63"/>
        <stop offset=".7" stop-color="#9a8468"/>
        <stop offset=".88" stop-color="#7d6a55"/>
        <stop offset="1" stop-color="#6a5446"/>
      </linearGradient>
    </defs>
    <rect role="img" aria-label="Faded apartment courtyard photo" width="758" height="232" fill="url(#heroFade)"/>
    <path role="img" aria-label="Modern brick apartment building photo" d="M544 0 H758 V232 H455 C470 150 500 80 544 0 Z" fill="url(#heroPhoto)"/>
    <path d="M520 0 H544 C500 80 470 150 455 232 H452 C420 170 440 80 520 0 Z" fill="#2a7db0"/>
  </svg>
  <div class="abs brand" style="left:57px;top:45px;font-size:11px"><i style="width:20px;height:20px;border-radius:3px"></i>NEXA HOLDINGS</div>
  <h1 class="abs">PRIVATE COMMERCIAL<br>REAL ESTATE INVESTMENT<br>AND DEVELOPMENT FIRM</h1>
  <div class="abs tag">Building together. Growing Together.</div>
</section>

<section class="abs about">
  <div class="abs pill" style="left:181px;top:10px;width:58px;height:18px;font-size:8px;line-height:18px">ABOUT US</div>
  <p>Corbel Estates is a private real estate firm that specializes in the procurement, development, management, and disposition of various commercial real estate asset types including multifamily, industrial, single-family, hospitality, self-storage, and flex. The firm effectuates its strategy by utilizing long-standing relationships to ascertain acquisition and development opportunities within a specific target market. Corbel Estates is currently focused on acquisition and development opportunities in the southern portion of the United States.</p>
</section>

<h2 class="abs projects-title">Projects</h2>
<p class="abs projects-intro">This is your Project Page. It's a great opportunity to help visitors understand the context and background of your latest work. Double click on the text box to start editing your content and make sure to add all the relevant details you want to share.</p>
<div class="abs view-all">View all</div>

<article class="abs card" style="left:167.5px">
  <div class="photo" role="img" aria-label="Apartment pool courtyard photo" style="background:linear-gradient(180deg,#4f9be4 0%,#9cc2e6 20%,#cdbda8 32%,#a89480 48%,#62c8e4 60%,#37acd6 78%,#c7d1d4 100%)"><div class="badge"><b></b>8 Lessons</div></div>
  <h3>Bayline Harbor Residences</h3><div class="type">Ground-up Development</div>
  <p>Class A Multifamily - 176 Units - 4 Story - 159,280 SF - 3 Acres</p>
</article>
<article class="abs card" style="left:310.5px">
  <div class="photo" role="img" aria-label="Evening lobby and garden walkway photo" style="background:linear-gradient(100deg,#1e2128 0%,#3b3f48 32%,#2d4a78 48%,#4a5a2a 62%,#8b8a3c 82%,#5a5f30 100%)"><div class="badge"><b></b>10 Lessons</div></div>
  <h3>Willowmere at Cedar Creek</h3><div class="type">Ground-up Development</div>
  <p>Class A Multifamily - 176 Units - 4 Story - 159,280 SF - 3 Acres</p>
</article>
<article class="abs card" style="left:453.5px">
  <div class="photo" role="img" aria-label="Hotel facade at dusk photo" style="background:linear-gradient(180deg,#1a4fd0 0%,#2e63d6 25%,#8a7a82 45%,#6e5a58 68%,#c9a060 84%,#3d5a2a 100%)"><div class="badge"><b></b>7 Lessons</div></div>
  <h3>Tint at Midtown</h3><div class="type">Ground-up Development</div>
  <p>Class A Multifamily - 176 Units - 4 Story - 159,280 SF - 3 Acres</p>
</article>

<div class="abs pill" style="left:325px;top:631px;width:110px;height:18px;font-size:8px;line-height:18px">CORPORATE PARTNERS</div>
<div class="abs partner" style="left:190px;color:var(--p-dark)">TORVEX</div>
<div class="abs partner" style="left:253px;color:var(--p-green)">ELMORA</div>
<div class="abs partner" style="left:317px;color:var(--p-navy)">Kestro</div>
<div class="abs partner" style="left:380px;color:var(--p-crimson)">HALVIK</div>
<div class="abs partner" style="left:444px;color:var(--p-gold)">BRISANE</div>
<div class="abs partner" style="left:507px;color:var(--p-green)">ELMORA</div>
<div class="abs partner" style="left:571px;color:var(--p-dark)">TORVEX</div>

<div class="abs city" role="img" aria-label="Blue-toned city skyline photo"></div>
<div class="abs map" role="img" aria-label="Office location map"></div>

<div class="info">
  <h4 style="top:921px">Inquiries</h4>
  <p style="left:167px;top:935px;width:242px">For any inquiries, questions or commendations, please call: (214) 555-0142 or fill out the following form</p>
  <h4 style="top:959px">Headquarters</h4>
  <p style="left:167px;top:973px">840 Linden Park Blvd. 5th Floor<br>Dallas, Texas 75219</p>
  <p style="left:317.5px;top:973px">info@corbelestates.com<br>Tel: (214) 555-0142</p>
  <h4 style="top:997px">Employment</h4>
  <p style="left:167px;top:1012px;width:242px">To apply for a job with Corbel Estates, please send a cover letter together with your C.V. to: info@corbelestates.com</p>
</div>

<form class="abs contact-card">
  <h2>CONTACT US</h2>
  <div class="abs" role="img" aria-label="Contact illustration" style="left:71px;top:29px;width:28px;height:24px;border-radius:50%;background:linear-gradient(135deg,#f3b34a,#2f5fb0 60%,#e2493d)"></div>
  <div class="field" style="top:69px">First Name</div>
  <div class="field" style="top:97.5px">Last Name</div>
  <div class="field" style="top:125.5px">Email</div>
  <div class="field" style="top:153.5px">Subject</div>
  <div class="field msg" style="top:179px;height:35px">Message</div>
  <div class="submit">Submit</div>
</form>

<footer class="abs footer">
  <div class="abs brand" style="left:170px;top:33px;font-size:6.2px;color:var(--white)"><i style="width:11px;height:11px;border-radius:2px;background:var(--white)"></i>NEXA HOLDINGS</div>
  <p class="lead">For any inquiries, questions or commendations, please call: (214) 555-0142 or fill out the following form</p>
  <h5>Contact</h5>
  <div class="f-item" style="top:44px">
    <svg width="8" height="8" viewBox="0 0 8 8"><rect width="8" height="8" rx="1.5" fill="#fff"/><path d="M2.3 1.8l1 1-.5.7c.3.7.8 1.2 1.5 1.5l.7-.5 1 1-.6.8C3.7 6.2 1.8 4.3 1.5 2.4z" fill="#2a7db0"/></svg>(214) 555-0142</div>
  <div class="f-item" style="top:58px">
    <svg width="8" height="8" viewBox="0 0 8 8"><rect width="8" height="8" rx="1.5" fill="#fff"/><rect x="1.8" y="2.5" width="4.4" height="3.2" rx=".4" fill="#2a7db0"/><path d="M1.9 2.7L4 4.3l2.1-1.6" stroke="#fff" stroke-width=".5" fill="none"/></svg>info@corbelestates.com</div>
  <div class="f-item" style="top:72px">
    <svg width="8" height="8" viewBox="0 0 8 8"><rect width="8" height="8" rx="1.5" fill="#fff"/><path d="M4 1.5a1.8 1.8 0 0 1 1.8 1.8C5.8 4.7 4 6.6 4 6.6S2.2 4.7 2.2 3.3A1.8 1.8 0 0 1 4 1.5z" fill="#2a7db0"/><circle cx="4" cy="3.3" r=".6" fill="#fff"/></svg><span>840 Linden Park Blvd. 5th Floor<br>Dallas, Texas 75219</span></div>
</footer>
</body>
</html>
```